B2B Energy Broker Website

Our current website looks amateur, we need something far more professional looking and advanced. Current website is www.halvorn-utilitypartners.com

```html
<!DOCTYPE html>
<html lang="en">
<head>
<meta charset="utf-8">
<title>Halvorn Utility Partners — Transparent Energy Savings</title>
<link href="https://fonts.googleapis.com/css2?family=Playfair+Display:wght@900&family=Mulish:wght@300;400;500;600;700&display=swap" rel="stylesheet">
<style>
:root{
  --stage:#5a6c97;
  --navy:#1d2550;
  --ink:#2a3350;
  --muted:#5d6478;
  --accent:#e8572e;
  --blue:#1588d8;
  --sky-top:#0f7fd6;
  --sky-mid:#5fb1ea;
  --sky-low:#d9e9f8;
  --page-top:#e4eefa;
  --page-bottom:#f7f9fd;
  --card:#ffffff;
  --partner:#6b7080;
  --green:#6cb33f;
}
*{margin:0;padding:0;box-sizing:border-box}
html,body{width:1200px;height:3125px;overflow:hidden}
body{background:var(--stage);font-family:"Mulish",sans-serif;color:var(--ink);position:relative}
.site{position:absolute;left:131px;top:127px;width:937px;height:2870px;border-radius:26px;overflow:hidden;
  background:linear-gradient(180deg,var(--page-top) 0%,var(--page-top) 35%,var(--page-bottom) 100%)}
.abs{position:absolute}
.hero{position:absolute;left:0;top:0;width:937px;height:760px;
  background:
   radial-gradient(ellipse 520px 260px at 50% 520px,#f4f7fb 0%,#cfd9e4 45%,rgba(207,217,228,0) 75%),
   radial-gradient(ellipse 700px 200px at 50% 720px,#f2f6fb 0%,rgba(242,246,251,0) 80%),
   linear-gradient(180deg,var(--sky-top) 0%,var(--sky-mid) 38%,var(--sky-low) 78%,var(--page-top) 100%)}
.brand{left:45px;top:30px;display:flex;align-items:center;gap:6px;color:#fff}
.brand-dot{width:22px;height:22px;border-radius:50%;border:3px solid #fff}
.brand-name{font-size:11px;font-weight:600;letter-spacing:1px;line-height:1.1}
.brand-name small{display:block;font-size:6px;font-weight:400;letter-spacing:0}
.nav{left:388px;top:36px;display:flex;gap:18px;font-size:8px;color:#dcecfb}
.nav .current{color:#fff;font-weight:700}
.nav-icon{top:30px;width:24px;height:24px;border-radius:50%;background:rgba(255,255,255,.25);display:flex;align-items:center;justify-content:center}
.btn{display:flex;align-items:center;justify-content:center;background:var(--accent);color:#fff;border-radius:14px;font-size:7.5px;font-weight:700}
.hero-title{left:0;width:937px;top:128px;text-align:center;font-family:"Playfair Display",serif;font-weight:900;font-size:36px;color:#fff}
.hero-sub{left:0;width:937px;top:180px;text-align:center;font-size:17px;font-weight:300;color:#fff}
.eyebrow{font-size:9px;letter-spacing:1.4px;color:var(--muted);text-align:center}
.eyebrow::after{content:"";display:block;width:28px;height:1.5px;background:var(--accent);margin:6px auto 0}
.eyebrow.left{text-align:left}
.eyebrow.left::after{margin-left:0}
.h2{font-family:"Playfair Display",serif;font-weight:900;color:var(--navy);font-size:26px;line-height:1.3}
.center{left:0;width:937px;text-align:center}
.body-text{font-size:7.6px;line-height:1.65;color:var(--muted)}
.card{position:absolute;background:var(--card);border-radius:18px}
.service{top:1034px;width:181px;height:195px;padding:26px 16px 0}
.service .dot{position:absolute;right:14px;top:14px;width:7px;height:7px;border-radius:50%;background:#b9d6f0}
.service h3,.feature h3{font-size:17px;font-weight:500;color:var(--navy);line-height:1.35;margin-top:10px}
.service p{font-size:7.3px;line-height:1.75;color:var(--muted);position:absolute;left:16px;right:12px;top:124px}
.partners{left:184px;top:1432px;width:577px;display:flex;justify-content:space-between;align-items:center}
.partner{display:flex;align-items:center;gap:5px;font-size:19px;font-weight:600;color:var(--partner)}
.partner i{width:14px;height:14px;border-radius:50%;background:var(--partner);display:block}
.pager{left:442px;top:1514px;display:flex;gap:11px}
.pager span{width:5px;height:5px;border-radius:50%;background:#c9d6e4}
.pager span:first-child{background:var(--blue)}
.art{position:absolute;border-radius:14px}
.feature{top:1916px;width:231px;height:214px;padding:26px 25px 0}
.feature p{font-size:7.3px;line-height:1.7;color:var(--muted);margin-top:30px}
.contact-row{left:221px;top:2670px;width:497px;display:flex;justify-content:space-between;font-size:7.3px;font-weight:600;color:var(--ink)}
.contact-row span{display:flex;align-items:center;gap:5px}
.footer{top:2742px;font-size:7.3px;color:var(--muted)}
</style>
</head>
<body>
<main class="site">
  <section class="hero" role="img" aria-label="Photograph of a snow-capped mountain peak rising above clouds under a bright blue sky"></section>

  <header>
    <div class="abs brand"><span class="brand-dot"></span><span class="brand-name">HALVORN<small>utility partners</small></span></div>
    <nav class="abs nav"><span class="current">Home</span><span>About Us</span><span>Services</span><span>FAQs</span></nav>
    <div class="abs nav-icon" style="left:750px"><svg width="11" height="11" viewBox="0 0 24 24" fill="none" stroke="#fff" stroke-width="2"><path d="M5 3h4l2 5-3 2a12 12 0 0 0 6 6l2-3 5 2v4a2 2 0 0 1-2 2A17 17 0 0 1 3 5a2 2 0 0 1 2-2z"/></svg></div>
    <div class="abs nav-icon" style="left:784px"><svg width="11" height="11" viewBox="0 0 24 24" fill="none" stroke="#fff" stroke-width="2"><rect x="3" y="5" width="18" height="14" rx="2"/><path d="M3 7l9 6 9-6"/></svg></div>
    <div class="abs btn" style="left:819px;top:30px;width:77px;height:24px">Contact Us</div>
  </header>

  <h1 class="abs hero-title">Transparent Energy Savings</h1>
  <p class="abs hero-sub">Unbiased for your business</p>

  <section>
    <p class="abs eyebrow center" style="top:775px">OUR STORY</p>
    <h2 class="abs h2 center" style="top:810px;font-size:25px">Halvorn Utility Partners</h2>
    <p class="abs body-text" style="left:278px;width:381px;top:860px;text-align:center">Along with providing competitive business energy procurement, we run a complete service solution for your ongoing energy requirements. We can take total management of your bills, supplier relationship, renewals and more. If you are concerned about a more complex arrangement for your energy supply then we will endeavour to take over the time spent on it and allow you as much or as little involvement as you desire.</p>
    <div class="abs btn" style="left:431px;top:933px;width:77px;height:23px">About Us</div>
  </section>

  <section>
    <article class="card service" style="left:85px"><span class="dot"></span>
      <svg width="22" height="22" viewBox="0 0 24 24" fill="none" stroke="var(--blue)" stroke-width="1.6"><path d="M4 21V4a1 1 0 0 1 1-1h8a1 1 0 0 1 1 1v17M3 21h12M4 10h10M14 8h2a2 2 0 0 1 2 2v7a1.5 1.5 0 0 0 3 0V8l-3-3"/></svg>
      <h3>Commercial<br>Gas</h3><p>We offer an impartial review of your business gas requirements to ensure you are getting the best prices, service and management as a total package.</p></article>
    <article class="card service" style="left:281px"><span class="dot"></span>
      <svg width="22" height="22" viewBox="0 0 24 24" fill="none" stroke="var(--blue)" stroke-width="1.6"><path d="M9 18h6M10 21h4M12 3a6 6 0 0 0-3.5 10.9V16h7v-2.1A6 6 0 0 0 12 3z"/></svg>
      <h3>Commercial<br>Electricity</h3><p>We offer an impartial review of your business electricity requirements to ensure you are getting the best prices, service and management as a total package.</p></article>
    <article class="card service" style="left:477px"><span class="dot"></span>
      <svg width="22" height="22" viewBox="0 0 24 24" fill="none" stroke="var(--blue)" stroke-width="1.6"><path d="M14.7 6.3a4 4 0 0 0 5 5L21 13l-8 8-3-3 1.3-1.3-7-7A4 4 0 0 1 9 4l1.7 1.7"/></svg>
      <h3>Utility<br>Services</h3><p>We can provide a wide range of business utility management services to ensure your time and money is better spent.</p></article>
    <article class="card service" style="left:672px"><span class="dot"></span>
      <svg width="22" height="22" viewBox="0 0 24 24" fill="none" stroke="var(--blue)" stroke-width="1.6"><path d="M12 3s6 7 6 11a6 6 0 0 1-12 0c0-4 6-11 6-11z"/></svg>
      <h3>Commercial<br>Water</h3><p>The commercial water market has now been de-regulated. Speak to our team to find out how we can save you money on your water and waste bills.</p></article>
  </section>

  <section>
    <p class="abs eyebrow center" style="top:1308px">OUR PARTNERS</p>
    <h2 class="abs h2 center" style="top:1342px;font-size:24px">Our Client Trust Us</h2>
    <div class="abs partners">
      <span class="partner">Brightwell</span>
      <span class="partner"><i></i>Norvane</span>
      <span class="partner">Kestra Energy</span>
      <span class="partner">Lumora</span>
      <span class="partner"><i></i>Tidegate</span>
    </div>
    <div class="abs pager"><span></span><span></span><span></span><span></span></div>
  </section>

  <section class="card" style="left:85px;top:1597px;width:768px;height:280px">
    <div class="art" role="img" aria-label="Illustration of a woman working at a desk with a computer, a potted plant and a paper bird flying overhead" style="left:61px;top:37px;width:251px;height:207px;background:radial-gradient(ellipse at 50% 55%,#d7e6f4 0%,#eef4fa 60%,#fff 100%)"></div>
    <h2 class="abs h2" style="left:361px;top:70px;font-size:29px;line-height:1.3">Contact Halvorn<br>Now To Start Saving</h2>
    <p class="abs" style="left:361px;top:190px;display:flex;align-items:center;gap:12px;font-size:16px;color:var(--ink)">
      <svg width="20" height="20" viewBox="0 0 24 24" fill="none" stroke="var(--accent)" stroke-width="1.8"><path d="M5 3h4l2 5-3 2a12 12 0 0 0 6 6l2-3 5 2v4a2 2 0 0 1-2 2A17 17 0 0 1 3 5a2 2 0 0 1 2-2z"/></svg>0333 418 2760</p>
  </section>

  <section>
    <article class="card feature" style="left:85px">
      <svg width="30" height="30" viewBox="0 0 30 30" fill="none" stroke="var(--blue)" stroke-width="1.8"><rect x="3" y="14" width="6" height="13"/><rect x="12" y="18" width="6" height="9"/><rect x="21" y="4" width="6" height="23"/></svg>
      <h3>Market Trend<br>Analysis</h3><p>Our energy analysts monitor a live energy market curve to ensure you buy at the right time and save as much as possible.</p></article>
    <article class="card feature" style="left:354px">
      <svg width="32" height="30" viewBox="0 0 32 30" fill="none" stroke="var(--accent)" stroke-width="1.8"><circle cx="16" cy="9" r="4"/><circle cx="7" cy="6" r="3"/><circle cx="25" cy="6" r="3"/><path d="M8 26v-4a8 8 0 0 1 16 0v4zM2 18a5 5 0 0 1 6-4M30 18a5 5 0 0 0-6-4"/></svg>
      <h3>Direct<br>Relationships</h3><p>We hold direct relationships with over 18 major suppliers, we use these relationships to ensure you get the most from your supplier.</p></article>
    <article class="card feature" style="left:622px">
      <svg width="30" height="30" viewBox="0 0 30 30" fill="none" stroke="var(--green)" stroke-width="1.8"><path d="M3 27h24M6 27V14h8v13M14 27V4h11v23"/><path d="M18 9h3M18 14h3M18 19h3M9 18h2M9 22h2"/></svg>
      <h3>Industry<br>Experience</h3><p>Our two founders hold over 30 years industry experience between them and our staff are what we believe to be the best in the industry.</p></article>
  </section>

  <section>
    <div class="art" role="img" aria-label="Illustration of large orange FAQ letters with people sitting and standing around them using laptops and phones" style="left:146px;top:2245px;width:247px;height:212px;background:radial-gradient(ellipse at 50% 55%,#f0a48b 0%,#f6d3c6 45%,rgba(230,238,250,0) 80%)"></div>
    <p class="abs eyebrow left" style="left:467px;top:2245px">FAQS</p>
    <h2 class="abs h2" style="left:467px;top:2280px;font-size:25px;line-height:1.32">Why Should My Business Use<br>Halvorn Utility Partners?</h2>
    <p class="abs body-text" style="left:467px;top:2366px;width:318px">We provide an unbiased &amp; transparent cost effective solution to all your business energy needs. In essence, with over 3 decades experience in the UK energy Industry. We have both the expertise &amp; know how to manage your business energy requirements. Our philosophy is simple solutions with transparency.</p>
    <div class="abs btn" style="left:467px;top:2436px;width:78px;height:23px">View All</div>
  </section>

  <footer>
    <h2 class="abs h2 center" style="top:2578px;font-size:25px">Curious? Get In Touch</h2>
    <p class="abs center" style="top:2624px;font-size:7.6px;color:var(--muted)">We can't promise a reply but we'd love to hear your thoughts.</p>
    <div class="abs contact-row">
      <span><svg width="10" height="10" viewBox="0 0 24 24" fill="none" stroke="var(--muted)" stroke-width="2"><rect x="5" y="3" width="14" height="18"/><path d="M9 7h2M13 7h2M9 11h2M13 11h2"/></svg>12 Marlow Street Leicester, LE2 4QT</span>
      <span><svg width="10" height="10" viewBox="0 0 24 24" fill="none" stroke="var(--muted)" stroke-width="2"><path d="M5 3h4l2 5-3 2a12 12 0 0 0 6 6l2-3 5 2v4a2 2 0 0 1-2 2A17 17 0 0 1 3 5a2 2 0 0 1 2-2z"/></svg>0333 418 2760</span>
      <span><svg width="10" height="10" viewBox="0 0 24 24" fill="none" stroke="var(--muted)" stroke-width="2"><rect x="4" y="9" width="16" height="11"/><path d="M7 9V3h10v6M8 13h2M12 13h2M8 16h2M12 16h2"/></svg>0333 418 2760</span>
      <span><svg width="10" height="10" viewBox="0 0 24 24" fill="none" stroke="var(--muted)" stroke-width="2"><rect x="3" y="5" width="18" height="14"/><path d="M3 7l9 6 9-6"/></svg>info@halvorn-utilitypartners.com</span>
    </div>
    <p class="abs footer center">© Halvorn Utility Partners 2015 All Rights Reserved &nbsp;|&nbsp; Privacy Policy &nbsp;|&nbsp; Cookie Policy &nbsp;|&nbsp; Terms &amp; Conditions</p>
  </footer>
</main>
</body>
</html>
```